Managed Service Provider email

We need an email designed that advertises our Managed Services product. We have been in business 28 years. Managed Services includes proactive ticketing, Help desk support, server and workstation monitoring, data backup monitoring, spam protection, regular reports, Deskflow 240, telecom services, ISP management, vendor management and more.

Target Market(s)

Business owners, decision makers, IT, CTO

Industry/Entity Type

Information Technology

Colors

Designer to choose colors to be used in the design.

Requirements
Must have
• Bullet points with included services. Mention of 28 years in business.
Nice to have
• We'd love our designer to read up on what an MSP (Managed Service Provider) does and use that information to find/create content for our email project.
Should not have
• A picture of a computer with a thermometer in its mouth.

```html
<!DOCTYPE html>
<html lang="en">
<head>
<meta charset="utf-8">
<title>Larch Network Services – Managed Services Email</title>
<link rel="stylesheet" href="https://fonts.googleapis.com/css2?family=Lato:wght@400;700&family=Raleway:wght@400;600&family=Exo+2:wght@600&display=swap">
<style>
:root{
  --page:#efefef;
  --white:#ffffff;
  --ink:#2b2b2b;
  --muted:#8a8a8a;
  --blue:#1a7fd4;
  --band:#1f6dbf;
  --orange:#ff6a3d;
  --navy-1:#0e3a66;
  --navy-2:#2d6ea8;
  --night-1:#05081a;
  --night-2:#1b2c55;
  --black:#000000;
}
*{box-sizing:border-box;margin:0;padding:0}
html,body{width:1200px;height:1200px;overflow:hidden;background:var(--page);font-family:"Lato",sans-serif;color:var(--ink)}
.preheader{position:absolute;top:31px;left:0;width:1200px;text-align:center;font-size:5.5px;color:var(--muted)}
.preheader a{color:var(--muted)}
.email{position:absolute;left:446px;top:53px;width:305px;background:var(--white)}
.hero{position:relative;height:191px;overflow:hidden}
.hero-photo{position:absolute;inset:0;background:linear-gradient(160deg,var(--navy-1),var(--navy-2) 45%,#0b2b52)}
.brand{position:absolute;top:24px;width:100%;text-align:center;color:var(--white);font-family:"Exo 2",sans-serif}
.brand-name{font-size:34px;line-height:30px;font-weight:600;letter-spacing:1px}
.brand-sub{font-size:10px;letter-spacing:.5px;margin-top:1px;font-weight:600}
.tagline{position:absolute;left:39px;top:98px;width:228px;height:44px;text-align:center;color:var(--white);font-family:"Raleway",sans-serif}
.tagline::before,.tagline::after{content:"";position:absolute;top:0;width:14px;height:44px;border:1px solid var(--white)}
.tagline::before{left:0;border-right:none}
.tagline::after{right:0;border-left:none}
.tagline-main{font-size:13px;margin-top:6px}
.tagline-sub{font-size:10.5px;margin-top:3px}
.accent{color:var(--orange)}
.intro{height:275px;text-align:center;padding-top:16px}
.section-title{font-family:"Raleway",sans-serif;color:var(--blue);font-size:15px;font-weight:400}
.copy{font-size:7.5px;line-height:11.6px;margin:9px auto 0;width:260px}
.services{list-style:none;text-align:left;margin:13px 0 0 56px}
.services li{font-size:5.5px;height:15.2px;line-height:8px;text-transform:uppercase;position:relative;padding-left:11px}
.services li::before{content:"";position:absolute;left:1px;top:1.5px;width:5px;height:5px;background:var(--orange);transform:rotate(45deg)}
.copy-2{margin-top:8px;width:270px}
.btn{display:inline-block;background:var(--orange);color:var(--white);border-radius:12px;font-size:8.5px;text-decoration:none;text-align:center}
.btn-lg{width:94px;height:23px;line-height:23px}
.intro .btn{margin-top:15px}
.band{position:relative;height:19px;background:var(--band);color:var(--white);text-align:center;font-size:7px;font-weight:700;line-height:19px}
.band::after{content:"";position:absolute;left:144px;bottom:-8px;border-left:8px solid transparent;border-right:8px solid transparent;border-top:8px solid var(--band)}
.specialties{height:210px;display:flex;gap:5.6px;padding:22px 16px 0}
.card{width:64px}
.card-photo{height:64px;background:linear-gradient(135deg,#1b2230,#4a78b8 55%,#20252d)}
.card-photo.warm{background:linear-gradient(135deg,#3b2a18,#c39a5a 50%,#1d2a3f)}
.card-title{font-size:6.8px;line-height:9px;margin-top:11px;height:25px;font-weight:400}
.card-title.strong{font-weight:700}
.card-text{font-size:5.4px;line-height:9px;color:var(--muted);height:49px}
.btn-sm{width:58px;height:15px;line-height:15px;font-size:5.5px;border-radius:8px}
.cta{position:relative;height:130px;text-align:center;color:var(--white);overflow:hidden}
.cta-photo{position:absolute;inset:0;background:linear-gradient(180deg,var(--night-1),var(--night-2) 70%,#2a3660)}
.cta-inner{position:relative;padding-top:20px;font-family:"Raleway",sans-serif}
.cta-title{font-size:13.5px;font-weight:600}
.cta-text{font-size:7.8px;line-height:11.2px;margin:5px auto 0;width:230px}
.cta .btn{margin-top:8px;font-family:"Lato",sans-serif}
.products{height:190px;text-align:center;padding-top:17px}
.partners{display:flex;justify-content:space-between;align-items:center;padding:0 16px;margin-top:20px;height:24px}
.partners-2{justify-content:center;gap:38px;margin-top:22px}
.partner{font-size:12px;font-weight:700}
.p-red{color:#d8232a}
.p-blue{color:#1869b2}
.p-slate{color:#4a5560}
.p-navy{color:#1f3f70}
.products .btn{margin-top:20px}
.footer{height:100px;background:var(--black);color:var(--white);text-align:center;padding-top:21px}
.social{display:flex;justify-content:center;gap:19.6px}
.social span{width:22px;height:22px;border-radius:50%;background:var(--white)}
.footer-note{font-size:6.3px;margin-top:6px;font-weight:700}
.footer-links{font-size:6.3px;margin-top:8px}
.copyright{font-size:6.3px;margin-top:8px;text-decoration:underline;font-weight:700}
</style>
</head>
<body>
<p class="preheader">Have trouble reading this email? <a href="#">View Online</a></p>
<main class="email">
  <header class="hero">
    <div class="hero-photo" role="img" aria-label="Blue-toned photo of a modern glass-roofed building interior"></div>
    <div class="brand">
      <div class="brand-name">Larch</div>
      <div class="brand-sub">network services</div>
    </div>
    <div class="tagline">
      <p class="tagline-main">Your Local, <span class="accent">Friendly It Department</span></p>
      <p class="tagline-sub">Managed Service Provider for <span class="accent">28 Years</span></p>
    </div>
  </header>

  <section class="intro">
    <h2 class="section-title">Decades of Service</h2>
    <p class="copy">Since we began installing business phone systems in 1990, Larch Communications has a long history of providing telecommunications services to Southwest Missouri Businesses.</p>
    <ul class="services">
      <li>Wireless surveys, design, and implementation</li>
      <li>Server sales and implementation - Corvell</li>
      <li>Workstation and laptop sales and installation - Corvell</li>
      <li>Computer hardware upgrades</li>
      <li>Switching | network engineering</li>
      <li>Firewalls and web filtering</li>
    </ul>
    <p class="copy copy-2">Lorem ipsum dolor sit amet, consectetur adipiscing elit. Donec elementum diam vel lectus pulvinar sodales. Fusce at quam et elit congue sodales. Integer porta sapien eu velit euismod scelerisque.</p>
    <a class="btn btn-lg" href="#">View More</a>
  </section>

  <div class="band">WE SPECIALIZE IN</div>

  <section class="specialties">
    <article class="card">
      <div class="card-photo" role="img" aria-label="Server rack with blue network cables"></div>
      <h3 class="card-title strong">Managed<br>IT Services</h3>
      <p class="card-text">Lorem ipsum dolor sit amet, consectetur adipiscing elit. Donec elementum diam vel lectus pulvinar...</p>
      <a class="btn btn-sm" href="#">Read More</a>
    </article>
    <article class="card">
      <div class="card-photo warm" role="img" aria-label="Wall-mounted phone system wiring"></div>
      <h3 class="card-title">Business<br>Phone System</h3>
      <p class="card-text">Lorem ipsum dolor sit amet, consectetur adipiscing elit. Donec elementum diam vel lectus pulvinar...</p>
      <a class="btn btn-sm" href="#">Read More</a>
    </article>
    <article class="card">
      <div class="card-photo warm" role="img" aria-label="Network equipment cabinet"></div>
      <h3 class="card-title">Network<br>Maintenanace</h3>
      <p class="card-text">Lorem ipsum dolor sit amet, consectetur adipiscing elit. Donec elementum diam vel lectus pulvinar...</p>
      <a class="btn btn-sm" href="#">Read More</a>
    </article>
    <article class="card">
      <div class="card-photo warm" role="img" aria-label="Cabling installation in a server room"></div>
      <h3 class="card-title">Cabling installation<br>Maintenance</h3>
      <p class="card-text">Lorem ipsum dolor sit amet, consectetur adipiscing elit. Donec elementum diam vel lectus pulvinar...</p>
      <a class="btn btn-sm" href="#">Read More</a>
    </article>
  </section>

  <section class="cta">
    <div class="cta-photo" role="img" aria-label="City skyline at night over water"></div>
    <div class="cta-inner">
      <h2 class="cta-title">Get us now!</h2>
      <p class="cta-text">Lorem ipsum dolor sit amet, consectetur adipiscing elit. Maecenas consequat rhoncus ligula, vestibulum convallis velit hendrerit eu. Integer porta enim tellus, ac ultricies.</p>
      <a class="btn btn-lg" href="#">Contact us</a>
    </div>
  </section>

  <section class="products">
    <h2 class="section-title">Our Products</h2>
    <div class="partners">
      <span class="partner p-red">Veyra</span>
      <span class="partner p-blue">Corvell</span>
      <span class="partner p-slate">Northgate Soft</span>
    </div>
    <div class="partners partners-2">
      <span class="partner p-navy">Omnilink</span>
      <span class="partner p-red">Tessaro</span>
    </div>
    <a class="btn btn-lg" href="#">View More</a>
  </section>

  <footer class="footer">
    <div class="social" aria-label="Social links">
      <span></span><span></span><span></span><span></span>
    </div>
    <p class="footer-note">You are currently subscibed to receive email updates from Larch Network Services.</p>
    <p class="footer-links">Unsubscribe | help | Contact Us | Privacy Policy | View Online</p>
    <p class="copyright">Copyright © 2017 Larch Network Services., All rights reserved.</p>
  </footer>
</main>
</body>
</html>
```